Brookhollow dog Kennel -Loyalty Card

We are a bod boarding and training Kennel located in Egypt and we would like to design a member loyalty card. The card need to be fun, funky. I would like the logo to appear on the card. On the back side we will list the benefits and on the bottom side of the card will will have the logos of our partner companies

Target Market(s)

clientele from dog lovers. Age 25 and above. 65% women.

Industry/Entity Type

Training

Font styles to use
Sans Serif

Colors
0555a3
33a6d7
0792cd

Requirements
Must have
• Brookhollow Logo and bleu colours.
Nice to have
• a dog figure
Should not have
• dark serious colours or aggressive looking dogs or dog breeds

```html
<!DOCTYPE html>
<html lang="en">
<head>
<meta charset="utf-8">
<title>Brookhollow dog Kennel – Loyalty Card</title>
<link rel="stylesheet" href="https://fonts.googleapis.com/css2?family=Baloo+2:wght@400;600;700&display=swap">
<style>
  :root {
    --bg: #e4eef5;
    --navy: #0555a3;
    --sky: #33a6d7;
    --azure: #0792cd;
    --sun: #f5a623;
    --white: #ffffff;
  }
  * { box-sizing: border-box; margin: 0; padding: 0; }
  html, body { width: 1200px; height: 900px; overflow: hidden; }
  body {
    background: var(--bg);
    font-family: "Baloo 2", sans-serif;
    color: var(--white);
    display: flex;
    align-items: center;
    justify-content: center;
    gap: 40px;
  }
  .card {
    position: relative;
    width: 560px;
    height: 320px;
    background: var(--navy);
    border-radius: 18px;
    overflow: hidden;
    box-shadow: 0 8px 20px rgba(5, 85, 163, 0.25);
  }
  .band { position: absolute; left: 0; right: 0; }

  .brand {
    position: absolute;
    display: flex;
    align-items: center;
    gap: 8px;
    font-weight: 700;
    font-size: 24px;
    line-height: 1;
    color: var(--white);
  }
  .brand-dot { width: 16px; height: 16px; border-radius: 50%; background: var(--sun); flex: none; }

  /* back: benefits and partners */
  .card-back .band-main { top: 28%; height: 50%; background: var(--azure); }
  .card-back .band-strip { top: 78%; height: 3%; background: var(--sky); }
  .card-back .band-foot { top: 81%; bottom: 0; background: var(--white); }
  .card-back .brand { top: 34px; left: 30px; }
  .card-back .card-label {
    position: absolute; top: 36px; right: 30px;
    font-size: 14px; font-weight: 600; letter-spacing: 1px;
    text-transform: uppercase; color: var(--sky);
  }
  .benefits {
    position: absolute; top: 104px; left: 30px; right: 30px;
    list-style: none;
    display: grid; grid-template-columns: 1fr 1fr; gap: 6px 24px;
    font-size: 15px; font-weight: 600; line-height: 1.3;
  }
  .benefits li { display: flex; align-items: center; gap: 8px; }
  .benefits svg { width: 14px; height: 14px; flex: none; }
  .partners {
    position: absolute; left: 30px; right: 30px; bottom: 14px;
    display: flex; justify-content: space-between;
  }
  .partner { width: 72px; height: 30px; border-radius: 8px; background: var(--sky); opacity: 0.55; }

  /* front: member details */
  .card-front .band-main { top: 40%; bottom: 10%; background: var(--azure); }
  .card-front .band-strip { top: 90%; height: 3%; background: var(--sky); }
  .card-front .brand { top: 84px; right: 30px; }
  .card-front .card-label {
    position: absolute; top: 28px; left: 30px;
    font-size: 14px; font-weight: 600; letter-spacing: 1px;
    text-transform: uppercase; color: var(--sky);
  }
  .person { position: absolute; left: 30px; top: 136px; }
  .person-name { font-size: 24px; font-weight: 700; line-height: 1.05; }
  .person-title { font-size: 13px; font-weight: 400; line-height: 1.2; }

  .contact {
    position: absolute; right: 24px; top: 178px;
    list-style: none;
    font-size: 14px; line-height: 19px;
  }
  .contact li { display: flex; justify-content: flex-end; align-items: center; gap: 8px; white-space: nowrap; }
  .contact svg { width: 12px; height: 12px; fill: var(--white); flex: none; }
</style>
</head>
<body>

  <section class="card card-back" aria-label="Card back">
    <div class="band band-main"></div>
    <div class="band band-strip"></div>
    <div class="band band-foot"></div>
    <div class="brand"><span class="brand-dot"></span>Brookhollow</div>
    <p class="card-label">Member Benefits</p>
    <ul class="benefits">
      <li><svg viewBox="0 0 14 14"><circle cx="7" cy="7" r="7" fill="#f5a623"/><path d="M3.5 7l2.5 2.5 4.5-5" stroke="#fff" stroke-width="2" fill="none"/></svg>10% off every boarding stay</li>
      <li><svg viewBox="0 0 14 14"><circle cx="7" cy="7" r="7" fill="#f5a623"/><path d="M3.5 7l2.5 2.5 4.5-5" stroke="#fff" stroke-width="2" fill="none"/></svg>Free first training class</li>
      <li><svg viewBox="0 0 14 14"><circle cx="7" cy="7" r="7" fill="#f5a623"/><path d="M3.5 7l2.5 2.5 4.5-5" stroke="#fff" stroke-width="2" fill="none"/></svg>Priority holiday booking</li>
      <li><svg viewBox="0 0 14 14"><circle cx="7" cy="7" r="7" fill="#f5a623"/><path d="M3.5 7l2.5 2.5 4.5-5" stroke="#fff" stroke-width="2" fill="none"/></svg>Birthday treat for your dog</li>
      <li><svg viewBox="0 0 14 14"><circle cx="7" cy="7" r="7" fill="#f5a623"/><path d="M3.5 7l2.5 2.5 4.5-5" stroke="#fff" stroke-width="2" fill="none"/></svg>Every 10th night is free</li>
      <li><svg viewBox="0 0 14 14"><circle cx="7" cy="7" r="7" fill="#f5a623"/><path d="M3.5 7l2.5 2.5 4.5-5" stroke="#fff" stroke-width="2" fill="none"/></svg>Partner shop discounts</li>
    </ul>
    <div class="partners" aria-label="Partner companies">
      <span class="partner"></span><span class="partner"></span><span class="partner"></span><span class="partner"></span><span class="partner"></span>
    </div>
  </section>

  <section class="card card-front" aria-label="Card front">
    <div class="band band-main"></div>
    <div class="band band-strip"></div>
    <p class="card-label">Loyalty Card</p>
    <div class="brand"><span class="brand-dot"></span>Brookhollow</div>

    <div class="person">
      <p class="person-name">Daniel Mercer</p>
      <p class="person-title">Managing Director</p>
    </div>

    <ul class="contact">
      <li>123.456.7890
        <svg viewBox="0 0 12 12"><path d="M1 4c0-2 2-3 5-3s5 1 5 3v1H8V4H4v1H1z M2 6h8l1 5H1z"/></svg></li>
      <li>123.456.7890
        <svg viewBox="0 0 12 12"><path d="M3 1h6v3H3z M1 4h10v7H1z"/></svg></li>
      <li>info@youremail.com
        <svg viewBox="0 0 12 12"><path d="M0 2h12v1L6 7 0 3z M0 4.5l6 4 6-4V10H0z"/></svg></li>
      <li>www.website.com
        <svg viewBox="0 0 12 12"><path d="M4 8l4-4 1 1-4 4z M1 7l2-2 1 1-2 2 2 2 2-2 1 1-2 2q-1 1-2 0L1 9q-1-1 0-2z M11 5L9 7 8 6l2-2-2-2-2 2-1-1 2-2q1-1 2 0l2 2q1 1 0 2z"/></svg></li>
      <li>1234, Address Goes Here, Country Name, 123456
        <svg viewBox="0 0 12 12"><path d="M6 0a4 4 0 0 1 4 4c0 3-4 8-4 8S2 7 2 4a4 4 0 0 1 4-4zm0 2.5a1.5 1.5 0 1 0 0 3 1.5 1.5 0 0 0 0-3z"/></svg></li>
    </ul>
  </section>

</body>
</html>
```